Kraft Eco-friendly pouch back imprint

Updating the design imprint on the back of our eco-friendly kraft stand up pouches. The current package back is a story letter but we want to change it to be more visually eye catching and make better use of buzzwords and graphics. I've uploaded a PDF with the current graphic so that key buzz words and thoughts could be pulled and highlighted.

The printing will be done in black and white, so don't spend time with colors. The imprint area is approximately 7" high x 5" wide.

I definitely want our logo at the top of the package, and I'm attaching two options.

Our mission is to be the Healthiest Pet Bakery in the U.S. That needs to be another point of emphasis.

Other potential buzzwords or bullets include:
Artisan Recipes
Simple Ingredients
No corn, wheat, soy, GMOs, or preservatives
Handcrafted
Locally sourced (Pacific NW)
Eco-conscious company
Updates

The system only allowed 24 hours. That is a ridiculously short time window.

Target Market(s)

Pet parents seeking natural, healthy products

Industry/Entity Type

independent pet channel

Colors

Designer to choose only greyscale colors for use in the design.

Requirements
Must have
• Logo, Mission, buzz words, graphics

```html
<!DOCTYPE html>
<html lang="en">
<head>
<meta charset="utf-8">
<title>Tails Hearth Bakery – Pouch Back Imprint</title>
<link rel="stylesheet" href="https://fonts.googleapis.com/css2?family=Mulish:wght@400&family=Pathway+Gothic+One&display=swap">
<style>
  :root {
    --ink: #1f1f1f;
    --ink-soft: #444444;
    --line: #7a7a7a;
    --art: #c9c9c9;
    --paper: #ffffff;
    --backdrop: #ffffff;
  }
  * { box-sizing: border-box; margin: 0; padding: 0; }
  html, body { width: 1200px; height: 998px; overflow: hidden; background: var(--backdrop); }
  ul, li { list-style: none; }
  .imprint {
    position: absolute; left: 270px; top: 37px;
    width: 660px; height: 924px;
    background: var(--paper);
    border: 1px solid var(--ink-soft);
    color: var(--ink);
    font-family: "Mulish", sans-serif;
  }
  .imprint > * { position: absolute; }
  .headline {
    font-family: "Pathway Gothic One", sans-serif;
    font-weight: 400; color: var(--ink); line-height: 1; white-space: nowrap;
  }
  .body-copy { font-size: 16px; line-height: 20.5px; color: var(--ink); }
  .rule { height: 0; border-top: 1.5px solid var(--line); }
  .art { background: var(--art); border-radius: 4px; }
  .dot { width: 5px; height: 5px; border-radius: 50%; background: var(--ink); }

  .brand-mark { left: 87px; top: 70px; width: 76px; height: 76px; border-radius: 50%; border: 2px solid var(--ink); }
  .brand-name { left: 180px; top: 88px; font-size: 38px; line-height: 1.1; color: var(--ink); white-space: nowrap; }

  .story { left: 82px; top: 201px; width: 360px; }
  .launch-art { left: 440px; top: 198px; width: 76px; height: 84px; background: linear-gradient(135deg, #d8d8d8, #b5b5b5); border-radius: 40% 6px 40% 6px; }
  .launch-year { left: 514px; top: 240px; font-size: 42px; }

  .rule-story { left: 83px; top: 296px; width: 490px; }

  .flag-art { left: 92px; top: 312px; width: 113px; height: 62px; background: linear-gradient(180deg, #e0e0e0, #bdbdbd); }
  .mission-title { right: 87px; top: 314px; font-size: 36px; }
  .mission-line { right: 87px; top: 351px; font-size: 15.5px; line-height: 18px; white-space: nowrap; }
  .rule-mission { left: 224px; top: 374px; width: 349px; }

  .pillars-a { left: 83px; top: 393px; font-size: 37px; }
  .pillar-dot { left: 308px; top: 409px; }
  .pillars-b { right: 87px; top: 393px; font-size: 37px; }

  .free-from { left: 83px; top: 440px; width: 490px; height: 86px; display: flex; align-items: center; justify-content: space-between; }
  .free-item { position: relative; width: 84px; height: 84px; border-radius: 50%; border: 1.5px solid var(--line); }
  .free-item .icon-art { position: absolute; left: 8px; top: 14px; width: 30px; height: 56px; border-radius: 15px; background: var(--art); }
  .free-item .label { position: absolute; left: 38px; top: 12px; width: 40px; font-family: "Pathway Gothic One", sans-serif; color: var(--ink-soft); text-align: center; line-height: 1; }
  .free-item .label b { display: block; font-weight: 400; font-size: 31px; }
  .free-item .label small { display: block; font-size: 19px; margin-top: 2px; }
  .free-link { flex: 1; height: 0; border-top: 1.5px solid var(--line); margin: 0 10px; }

  .local-title { left: 82px; top: 543px; font-size: 36px; }
  .local-copy { left: 82px; top: 579px; width: 366px; text-align: justify; font-size: 15px; }
  .region-art { left: 448px; top: 545px; width: 118px; height: 117px; background: linear-gradient(160deg, #e4e4e4, #bcbcbc); clip-path: polygon(0 5%, 55% 0, 60% 55%, 100% 58%, 100% 88%, 20% 100%, 8% 60%); }
  .region-label { left: 514px; top: 549px; font-size: 22px; line-height: 0.95; text-align: right; color: var(--ink-soft); }

  .craft-a { left: 84px; top: 675px; font-size: 36px; }
  .craft-dot { left: 262px; top: 691px; }
  .craft-b { right: 86px; top: 675px; font-size: 36px; }
  .craft-copy { left: 80px; top: 713px; width: 496px; text-align: center; font-size: 14.5px; line-height: 20px; letter-spacing: -0.4px; }

  .rule-sign { left: 83px; top: 786px; width: 490px; }
  .pet-art { left: 83px; top: 795px; width: 94px; height: 62px; background: linear-gradient(180deg, #8a8a8a, #5e5e5e); border-radius: 40% 50% 20% 20%; }
  .sign-off { right: 87px; top: 797px; text-align: right; font-style: normal; }
</style>
</head>
<body>
  <article class="imprint">
    <div class="brand-mark" aria-hidden="true"></div>
    <div class="brand-name">Tails Hearth Bakery</div>

    <p class="story body-copy">Tails Hearth Bakery was acquired by a couple in Cedar Cove, WA in 2017 (originally founded in 2004) and who also own and operate two independent pet health food stores.</p>
    <div class="launch-art" role="img" aria-label="Line drawing of a rocket launching"></div>
    <div class="launch-year headline">2011</div>

    <div class="rule rule-story"></div>

    <div class="flag-art art" role="img" aria-label="Line drawing of a waving U.S. flag"></div>
    <h2 class="mission-title headline">OUR MISSION</h2>
    <p class="mission-line">is to be the healthiest pet bakery in the U.S.A.</p>
    <div class="rule rule-mission"></div>

    <h2 class="pillars-a headline">ARTISAN RECIPES</h2>
    <span class="pillar-dot dot"></span>
    <h2 class="pillars-b headline">SIMPLE INGREDIENTS</h2>

    <ul class="free-from">
      <li class="free-item"><span class="icon-art" role="img" aria-label="Ear of corn drawing"></span><span class="label"><b>NO</b><small>CORN</small></span></li>
      <li class="free-link"></li>
      <li class="free-item"><span class="icon-art" role="img" aria-label="Wheat stalk drawing"></span><span class="label"><b>NO</b><small>WHEAT</small></span></li>
      <li class="free-link"></li>
      <li class="free-item"><span class="icon-art" role="img" aria-label="Soybean pod drawing"></span><span class="label"><b>NO</b><small>SOY</small></span></li>
      <li class="free-link"></li>
      <li class="free-item"><span class="icon-art" role="img" aria-label="Lab flask and test tube drawing"></span><span class="label"><b>NO</b><small>GMOs</small></span></li>
    </ul>

    <h2 class="local-title headline">LOCALLY SOURCED</h2>
    <p class="local-copy body-copy">Our treats are hand crafted using only the highest quality human grade ingredients, which are sourced as locally as possible in the Pacific Northwest.</p>
    <div class="region-art" role="img" aria-label="Outline map of the Pacific Northwest states and provinces"></div>
    <div class="region-label headline">PACIFIC<br>NW</div>

    <h2 class="craft-a headline">HANDCRAFTED</h2>
    <span class="craft-dot dot"></span>
    <h2 class="craft-b headline">ECO-CONSCIOUS COMPANY</h2>
    <p class="craft-copy body-copy">We focus on the environment and this package reflects our commitment to reducing our carbon pawprint. We hope that your furry friend enjoys our hand-crafted treats as much as we enjoy making them.</p>

    <div class="rule rule-sign"></div>
    <div class="pet-art" role="img" aria-label="Silhouette of a running retriever dog"></div>
    <address class="sign-off body-copy">
      Your friends @ Tails Hearth Bakery<br>
      www.tailshearthbakery.com<br>
      Harborview, WA &nbsp;&nbsp;866-555-TAIL
    </address>
  </article>
</body>
</html>
```